IT Consulting Business Card Design

We need a business card on our company name....which is a IT consulting and staffing company. We also train masters graduates in various IT courses. 70% of the time these cards will be handed out to the graduate students at the universities. 30% for our clients and business partners. We are uploading our company logo...would like to see something that matches our logo or blends with it. Please visit www.brightvaleworks.com for more details on logo and colors.

Target Market(s)

70% of the time these cards will be handed out to the graduate students at the universities. 30% for our clients and business partners.

Industry/Entity Type

Business

Contact Information for Business Card

Ravi Kondamuri
Vice-President
Bright Vale Works Inc
3807 Morrow Lane, Suite 412
East Brookridge, NJ 07315
ravi@brightvaleworks.com
Office : 1-866-219-3840 X 515
Cell number : 732-581-9034

Requirements
Nice to have
• may be company logo and name on the back of the card and detials on the other side...just a thought..!!

```html
<!DOCTYPE html>
<html lang="en">
<head>
<meta charset="utf-8">
<title>Bright Vale Works – Business Card</title>
<link rel="stylesheet" href="https://fonts.googleapis.com/css2?family=Crimson+Text:wght@400;600;700&display=swap">
<style>
  :root {
    --stage: #070a0a;
    --paper: #f2f5f5;
    --ink: #2e3133;
    --ink-soft: #3a3d40;
    --brand-red: #e8140f;
    --mark-grey: #c8cbcc;
  }
  * { margin: 0; padding: 0; box-sizing: border-box; }
  html, body {
    width: 1200px; height: 1000px; overflow: hidden;
    background: var(--stage);
  }
  body { position: relative; font-family: "Crimson Text", Georgia, serif; color: var(--ink); }
  .card {
    position: absolute;
    background: var(--paper);
  }
  .card--front { left: 27px; top: 20px; width: 828px; height: 485px; }
  .card--back { left: 374px; top: 513px; width: 805px; height: 470px; }

  .holder-name {
    position: absolute; left: 53px; top: 42px;
    font-size: 50px; font-weight: 400; line-height: 1;
    color: var(--ink);
    text-shadow: 2px 3px 4px rgba(0,0,0,0.35);
  }
  .holder-title {
    position: absolute; left: 59px; top: 104px;
    font-size: 22px; line-height: 1; color: var(--ink-soft);
  }
  .address {
    position: absolute; left: 59px; top: 218px;
    font-size: 23px; line-height: 30px; color: var(--ink-soft);
    font-style: normal;
  }
  .contact-row {
    position: absolute; left: 59px; top: 408px;
    display: flex; gap: 26px;
    font-size: 17px; line-height: 1; color: var(--ink);
  }
  .brand-spot {
    position: absolute; left: 508px; top: 82px;
    width: 250px; display: flex; flex-direction: column; align-items: center; gap: 18px;
  }
  .brand-spot .brand-name {
    font-size: 24px; font-weight: 700; color: var(--brand-red);
  }
  .brand-lockup {
    position: absolute; left: 94px; top: 134px;
    display: flex; align-items: center; gap: 36px;
  }
  .brand-lockup .brand-name {
    font-size: 48px; font-weight: 700; color: var(--ink); letter-spacing: 0.5px;
    white-space: nowrap;
  }
  .brand-dot { display: block; }
</style>
</head>
<body>
  <section class="card card--front">
    <h1 class="holder-name">Ravi Kondamuri</h1>
    <p class="holder-title">Vice-President</p>
    <address class="address">
      Bright Vale Works Inc<br>
      3807 Morrow Lane,<br>
      Suite 412 East Brookridge, NJ 07315
    </address>
    <div class="contact-row">
      <span class="contact-office">Office : 1-866-219-3840 X 515</span>
      <span class="contact-email">ravi@brightvaleworks.com</span>
      <span class="contact-cell">Cell number : 732-581-9034</span>
    </div>
    <div class="brand-spot">
      <svg class="brand-dot" width="190" height="190" viewBox="0 0 190 190" aria-hidden="true">
        <circle cx="95" cy="95" r="95" fill="var(--mark-grey)"/>
      </svg>
      <span class="brand-name">Bright Vale Works</span>
    </div>
  </section>

  <section class="card card--back">
    <div class="brand-lockup">
      <svg class="brand-dot" width="160" height="160" viewBox="0 0 160 160" aria-hidden="true">
        <circle cx="80" cy="80" r="80" fill="var(--mark-grey)"/>
      </svg>
      <span class="brand-name">BRIGHT VALE WORKS</span>
    </div>
  </section>
</body>
</html>
```